One-Page Flat Design for SEO Company [2 DAYS]

We need a one-page flat design for our SEO company. Our current website is http://www.rankloft.com/. We are looking to completely re-design the site using new flat design techniques.
Below are some examples of the type of style we're going after:
http://quormel.com/
http://tobyrand.co.uk/
https://pentaly.co/
http://milesporter.me/
As you can see- flat, clean, minimal. It is very important you follow this type of style.
For colour scheme, you may use one of the pre-made colour palettes from here:
http://www.vornacle.com/blog/inspiration/24-flat-designs-with-compelling-color-palettes
I've attached a wireframe to be followed.
Hi,

```html
<!DOCTYPE html>
<html lang="en">
<head>
<meta charset="utf-8">
<title>RankLoft — SEO Services</title>
<link rel="stylesheet" href="https://fonts.googleapis.com/css2?family=Lato:wght@400;700;900&family=Open+Sans:wght@400;600&display=swap">
<style>
:root{
  --paper:#ececea;
  --ink:#2b2b2b;
  --muted:#7a7a7a;
  --white:#ffffff;
  --hero-a:#4a3a2e;
  --hero-b:#8a6a4a;
  --hero-c:#2e2824;
  --sky:#29b6e6;
  --sun:#f5bd0d;
  --leaf:#6dbf3a;
  --teal:#2aac93;
  --teal-btn:#1ea59a;
  --plum:#5a2678;
  --tangerine:#f36d21;
  --cobalt:#1d6fbc;
  --gold:#f2b01e;
  --card:#e8edf1;
  --rule:#cfd6dc;
  --coral:#f77a7a;
  --lagoon:#56c2d6;
  --deep-lagoon:#3a7f89;
  --coal:#383636;
  --ring:#d8d8d8;
  --orange-label:#f39a2b;
  --green-label:#6dbf3a;
  --blue-label:#29b6e6;
}
*{box-sizing:border-box;margin:0;padding:0}
html,body{width:1200px;height:3243px;overflow:hidden}
body{position:relative;background:var(--paper);font-family:"Open Sans",Arial,sans-serif;color:var(--ink)}
.abs{position:absolute}
.heading{font-family:"Lato",Arial,sans-serif;font-weight:900;text-transform:uppercase;text-align:center;left:0;width:1200px}

/* header */
.site-header{position:absolute;left:0;top:0;width:1200px;height:68px;z-index:2}
.logo{position:absolute;left:108px;top:14px;font-family:"Lato",sans-serif;font-weight:700;font-size:36px;letter-spacing:4px;color:var(--white)}
.nav{position:absolute;left:500px;top:0;display:flex}
.nav a{display:block;padding:14px 20px 0;height:40px;font-family:"Lato",sans-serif;font-weight:700;font-size:15px;color:var(--white);text-decoration:none;letter-spacing:1px}
.nav a.active{border-top:4px solid var(--teal);padding-top:10px}

/* hero */
.hero{position:absolute;left:0;top:0;width:1200px;height:551px;background:linear-gradient(100deg,var(--hero-c) 0%,var(--hero-a) 35%,var(--hero-b) 60%,var(--hero-c) 100%)}
.hero-shade{position:absolute;inset:0;background:rgba(20,20,20,.35)}
.tile{position:absolute;color:var(--white);font-family:"Lato",sans-serif;font-size:27px}
.tile span{position:absolute;right:14px;bottom:10px}
.tile-main{left:109px;top:136px;width:386px;height:203px;background:var(--sky)}
.tile-support{left:109px;top:348px;width:189px;height:118px;background:var(--sun);font-size:22px}
.tile-innov{left:307px;top:348px;width:188px;height:118px;background:var(--leaf);font-size:22px}
.tile svg{position:absolute}
.hero-title{position:absolute;left:566px;top:184px;font-family:"Lato",sans-serif;font-weight:900;font-size:46px;line-height:52px;color:var(--white);text-transform:uppercase}
.hero-text{position:absolute;left:566px;top:306px;width:540px;font-size:18px;line-height:27px;color:#f0f0f0}
.btn-contact{position:absolute;left:884px;top:407px;width:207px;height:56px;background:var(--teal-btn);color:var(--white);font-family:"Lato",sans-serif;font-weight:900;font-size:20px;text-align:center;line-height:56px}

/* services */
.sub{font-size:16px;line-height:22px;color:var(--muted);text-align:center;left:0;width:1200px}
.feature{position:absolute;width:260px;text-align:center}
.feature .ring{width:177px;height:177px;margin:0 auto;border-radius:50%;background:var(--ring);padding:12px}
.feature .disc{width:153px;height:153px;border-radius:50%}
.feature .label{margin-top:22px;font-size:14px;text-transform:uppercase}
.feature p{margin:12px auto 0;width:200px;font-size:13px;line-height:17px;color:var(--muted)}

/* plans */
.plans{position:absolute;left:0;top:1076px;width:1200px;height:604px;background:var(--teal)}
.plans .heading{color:var(--white);top:38px;font-size:36px}
.plans .sub{top:90px;color:#e0f3ee}
.plan{position:absolute;top:147px;width:242px;height:404px;background:var(--card)}
.plan-head{height:76px;color:var(--white);text-align:center;font-family:"Lato",sans-serif}
.plan-head b{display:block;padding-top:12px;font-size:24px;font-weight:900;text-transform:uppercase}
.plan-head small{font-size:14px}
.plan h4{margin:20px 0 0 28px;font-family:"Lato",sans-serif;font-weight:900;font-size:16px}
.plan ul{list-style:none;margin:12px 24px 0 28px}
.plan li{font-size:13px;height:34px;line-height:34px;border-bottom:1px solid var(--rule)}
.plan .go{position:absolute;left:40px;bottom:26px;width:162px;height:40px;background:var(--leaf);color:var(--white);font-family:"Lato",sans-serif;font-weight:900;font-size:16px;text-align:center;line-height:40px;text-transform:uppercase}
.plan-featured{background:var(--white);box-shadow:0 4px 14px rgba(0,0,0,.3);height:408px}
.badge{position:absolute;left:-4px;top:-14px}

/* strip */
.strip{position:absolute;left:0;top:1680px;width:1200px;height:89px;background:var(--sun)}
.strip p{position:absolute;left:166px;top:28px;font-size:24px;color:var(--white)}
.strip .btn{position:absolute;left:843px;top:18px;width:192px;height:53px;background:var(--coral);color:var(--white);font-family:"Lato",sans-serif;font-weight:900;font-size:20px;text-align:center;line-height:53px}

/* contact */
.contact{position:absolute;left:0;top:2294px;width:1200px;height:654px;background:var(--lagoon)}
.contact .heading{top:30px;color:var(--white);font-size:38px}
.contact .addr{position:absolute;top:92px;left:0;width:1200px;text-align:center;color:var(--white);font-size:16px}
.form{position:absolute;left:183px;top:129px;width:834px;height:442px;background:var(--deep-lagoon)}
.field{position:absolute;background:var(--white);border-radius:4px;color:#9a9a9a;font-size:14px;padding:14px 16px}
.send{position:absolute;left:268px;top:366px;width:301px;height:41px;background:var(--coral);color:var(--white);font-family:"Lato",sans-serif;font-weight:700;font-size:18px;text-align:center;line-height:41px}
.socials{position:absolute;top:596px;left:0;width:1200px}
.socials span{position:absolute;font-family:"Lato",sans-serif;font-weight:700;font-size:21px;color:var(--white);transform:translateX(-50%)}

/* footer */
.site-footer{position:absolute;left:0;top:2948px;width:1200px;height:295px;background:var(--coal);text-align:center}
.site-footer .logo{position:static;display:block;padding-top:44px;font-size:44px}
.site-footer p{margin-top:12px;font-size:15px;line-height:22px;color:#cfcfcf}
.dot{position:absolute;top:188px;width:70px;height:70px;border-radius:50%}
</style>
</head>
<body>

<header class="site-header">
  <div class="logo">LOGO</div>
  <nav class="nav">
    <a class="active" href="#">HOME</a><a href="#">ABOUT</a><a href="#">WORK</a><a href="#">SERVICES</a><a href="#">TEAM</a><a href="#">CONTACT</a>
  </nav>
</header>

<section class="hero">
  <div class="hero-bg abs" style="inset:0" role="img" aria-label="Blurred photograph of a busy city street at dusk"></div>
  <div class="hero-shade"></div>
  <div class="tile tile-main">
    <svg width="110" height="110" viewBox="0 0 110 110" style="left:40px;top:26px" aria-hidden="true">
      <g stroke="#fff" stroke-width="6" stroke-linecap="round" fill="none">
        <circle cx="55" cy="52" r="22"/>
        <line x1="46" y1="82" x2="64" y2="82"/><line x1="48" y1="92" x2="62" y2="92"/>
        <line x1="55" y1="10" x2="55" y2="20"/><line x1="18" y1="52" x2="28" y2="52"/><line x1="82" y1="52" x2="92" y2="52"/>
        <line x1="27" y1="24" x2="34" y2="31"/><line x1="83" y1="24" x2="76" y2="31"/>
      </g>
    </svg>
    <span>Effective Solutions!</span>
  </div>
  <div class="tile tile-support">
    <svg width="44" height="40" viewBox="0 0 44 40" style="left:16px;top:14px" aria-hidden="true">
      <path d="M4 4h36v22H18l-9 9v-9H4z" fill="none" stroke="#fff" stroke-width="3" stroke-linejoin="round"/>
    </svg>
    <span>Support</span>
  </div>
  <div class="tile tile-innov">
    <svg width="48" height="44" viewBox="0 0 48 44" style="left:16px;top:12px" aria-hidden="true">
      <path d="M4 22L44 4 34 40 22 28zM22 28L44 4" fill="none" stroke="#fff" stroke-width="3" stroke-linejoin="round"/>
    </svg>
    <span>Innovations</span>
  </div>
  <h1 class="hero-title">Finally, SEO services<br>that actually work.</h1>
  <p class="hero-text">Top-notch SEO services that are guaranteed to boost your search engine rankings. 100% Searchly-friendly.</p>
  <div class="btn-contact">CONTACT US</div>
</section>

<section class="why">
  <h2 class="heading abs" style="top:598px;font-size:36px">Why choose RankLoft</h2>
  <p class="sub abs" style="top:656px">Fusce dapibus, tellus ac cursus commodo, tortor mauris condimentum.<br>Duis mollis, est non commodo luctus, nisi erat porttitor ligula, eget lacinia odio sem nec elit.</p>
  <div class="feature" style="left:203px;top:736px">
    <div class="ring"><div class="disc" style="background:#111" role="img" aria-label="Branding icon: eye over a folded map"></div></div>
    <div class="label" style="color:var(--orange-label)">Branding</div>
    <p>This is Pixelforge's version of Lorem Ipsum. Proin gravida nibh vel velit auctor aliquet. Aenean sollicitudin, lorem quis</p>
  </div>
  <div class="feature" style="left:477px;top:736px">
    <div class="ring"><div class="disc" style="background:var(--sky)" role="img" aria-label="Design icon: stylus on a drawing tablet"></div></div>
    <div class="label" style="color:var(--green-label)">Design</div>
    <p>This is Pixelforge's version of Lorem Ipsum. Proin gravida nibh vel velit auctor aliquet. Aenean sollicitudin, lorem quis</p>
  </div>
  <div class="feature" style="left:749px;top:736px">
    <div class="ring"><div class="disc" style="background:var(--sky)" role="img" aria-label="Development icon: desktop computer"></div></div>
    <div class="label" style="color:var(--blue-label)">Development</div>
    <p>This is Pixelforge's version of Lorem Ipsum. Proin gravida nibh vel velit auctor aliquet. Aenean sollicitudin, lorem quis</p>
  </div>
</section>

<section class="plans">
  <h2 class="heading abs">Select a booster plan</h2>
  <p class="sub abs">Neque porro quisquam est, qui dolorem ipsum quia dolor sit amet</p>

  <div class="plan" style="left:112px">
    <div class="plan-head" style="background:var(--plum)"><b>Personal</b><small>$9/Month</small></div>
    <h4>FEATURES</h4>
    <ul><li>Smells Fast</li><li>Has Bad Luck</li><li>Branding Superstar</li><li>Owns Four Cats</li><li>Vegetarian</li></ul>
    <div class="go">Get started</div>
  </div>
  <div class="plan" style="left:363px">
    <div class="plan-head" style="background:var(--tangerine)"><b>Professional</b><small>$16/Month</small></div>
    <h4>FEATURES</h4>
    <ul><li>Mediocre Hair</li><li>Incredible UI Designer</li><li>Wrinkley Clothes</li><li>Is Moving to California</li><li>Loses at Poker</li></ul>
    <div class="go">Get started</div>
  </div>
  <div class="plan plan-featured" style="left:601px;top:135px">
    <div class="plan-head" style="background:var(--cobalt)"><b>Business</b><small>$24/Month</small></div>
    <svg class="badge" width="70" height="70" viewBox="0 0 70 70" aria-hidden="true">
      <polygon fill="var(--gold)" points="35,2 42,12 54,8 56,20 68,24 62,35 68,46 56,50 54,62 42,58 35,68 28,58 16,62 14,50 2,46 8,35 2,24 14,20 16,8 28,12"/>
      <text x="35" y="33" text-anchor="middle" font-family="Lato,sans-serif" font-weight="900" font-size="11" fill="#fff" transform="rotate(-12 35 35)">BEST</text>
      <text x="35" y="45" text-anchor="middle" font-family="Lato,sans-serif" font-weight="900" font-size="11" fill="#fff" transform="rotate(-12 35 35)">VALUE</text>
    </svg>
    <h4>FEATURES</h4>
    <ul><li>Amazing Good Looks</li><li>Handsome Hazel Eyes</li><li>Loves to Cook</li><li>Gives Great Massages</li><li>Overall Happy Dude</li></ul>
    <div class="go">Get started</div>
  </div>
  <div class="plan" style="left:855px">
    <div class="plan-head" style="background:var(--gold)"><b>Enterprise</b><small>$40/Month</small></div>
    <h4>FEATURES</h4>
    <ul><li>Smells Like Ginger</li><li>Has Four Kids</li><li>Lives in the Country</li><li>Plays Guitar Pretty Well</li><li>Great Project Pilot</li></ul>
    <div class="go">Get started</div>
  </div>
</section>

<section class="strip">
  <p>Duis mollis est non commodo luctus nisi erat porttitor.</p>
  <div class="btn">BUTTON</div>
</section>

<section class="individual">
  <h2 class="heading abs" style="top:1813px;font-size:36px">Individual SEO services</h2>
  <p class="sub abs" style="top:1868px">usce dapibus, tellus ac cursus commodo, tortor mauris condimentum.<br>Duis mollis, est non commodo luctus, nisi erat porttitor ligula, eget lacinia odio sem nec elit.</p>
  <div class="feature" style="left:203px;top:1960px">
    <div class="ring"><div class="disc" style="background:#111" role="img" aria-label="Branding icon: eye over a folded map"></div></div>
    <div class="label" style="color:var(--orange-label)">Branding</div>
    <p>This is Pixelforge's version of Lorem Ipsum. Proin gravida nibh vel velit auctor aliquet. Aenean sollicitudin, lorem quis</p>
  </div>
  <div class="feature" style="left:477px;top:1960px">
    <div class="ring"><div class="disc" style="background:var(--leaf)" role="img" aria-label="Design icon: stylus on a drawing tablet"></div></div>
    <div class="label" style="color:var(--green-label)">Design</div>
    <p>This is Pixelforge's version of Lorem Ipsum. Proin gravida nibh vel velit auctor aliquet. Aenean sollicitudin, lorem quis</p>
  </div>
  <div class="feature" style="left:749px;top:1960px">
    <div class="ring"><div class="disc" style="background:var(--leaf)" role="img" aria-label="Development icon: desktop computer"></div></div>
    <div class="label" style="color:var(--blue-label)">Development</div>
    <p>This is Pixelforge's version of Lorem Ipsum. Proin gravida nibh vel velit auctor aliquet. Aenean sollicitudin, lorem quis</p>
  </div>
</section>

<section class="contact">
  <h2 class="heading abs">Get in touch</h2>
  <p class="addr">48 Larchmont Row, Fairhollow, OR 97402, United States of America. Tel: (541) 555-0182</p>
  <div class="form">
    <div class="field" style="left:53px;top:36px;width:354px;height:47px">Your Name</div>
    <div class="field" style="left:427px;top:36px;width:354px;height:47px">Your Email</div>
    <div class="field" style="left:53px;top:103px;width:728px;height:218px">Type your message...</div>
    <div class="send">SEND</div>
  </div>
  <div class="socials">
    <span style="left:389px">Friendly</span>
    <span style="left:528px">Chirpline</span>
    <span style="left:672px">Plusora</span>
    <span style="left:790px">Linkwork</span>
  </div>
</section>

<footer class="site-footer">
  <span class="logo">LOGO</span>
  <p>Fusce dapibus, tellus ac cursus commodo, tortor mauris condimentum.<br>Duis mollis, est non commodo luctus, nisi erat porttitor ligula.</p>
  <span class="dot" style="left:428px;background:#3b5a9a" aria-label="Friendly"></span>
  <span class="dot" style="left:561px;background:#29aae1" aria-label="Chirpline"></span>
  <span class="dot" style="left:702px;background:#111" aria-label="Plusora"></span>
</footer>

</body>
</html>
```